Pull Up Banner - Recruitment Company

We would like a design for a pull up banner.

For context: we are a recruitment business. We specialise in helping people in healthcare industry to find jobs in Australia.

I have come up with several ideas and text for the banner. Feel free to use the following as you see appropriate:

- Our logo (see attached)
- 'Healthcare Recruitment Agency'
- Some sort of imagine / cartoon of medical professionals (ie. doctor, nurse, physiotherapist, speech pathologist). A cartoon is more friendly than committing to a photo
- 'Empowering your next career move'
- 'Discover tailored opportunities based on your career preferences'
- Dot points (allied health, nursing, medical imaging)
- Contact info at the bottom including our website (www.pellatalent.com.au, our Instagram handle @pellatalent, Mobile: XXXX XXX XXX. The title section for contact information could be 'Get in touch:'

Feel free to submit a couple of designs and we can merge aspects that look good on your designs and find the perfect fit.
Thank you
Updates

Hello,

Thank you for your initial submissions to this project. I appreciate the time you've invested.

After reviewing the first attempt, I'd like to share some feedback and initial observations:

- Professionalism and engagement: Is the overall appearance of the banner professional? It's crucial that we have a high-quality design as this will represent our business.

- Image selection: The image (whether cartoon or real people) appears quite generic. Please consider submitting the banner with a few different photos in the middle for us to choose from. Ensure the image is a good fit and not simply a generic stock photo.

- Contact section: Kindly remove the phone number; we no longer wish to include it on the banner. Instead, please include our website (www.pellatalent.com.au) and Instagram handle (@pellatalent).

- Color scheme: White, black, and red/pink are preferred, or alternatively, blue. However, please avoid incorporating too many different colors as it may detract from the professional appearance.

We will be printing the design on a banner and require it to look professional and engaging.

Thank you once again for your submissions. I hope the feedback provided above is helpful.

Warm regards,

Target Market(s)

Allied Health Australia

Font styles to use
Serif

Colors
0054AA
0677BA
7BADD7
CADEEF
E8F1F8
0094D4
00A9DD
6FCCEA
C7EBF8
E9F6FB
EB3D1F
EC4F4E
F09395
F8D3D4
FCEDEE

```html
<!DOCTYPE html>
<html lang="en">
<head>
<meta charset="utf-8">
<title>Pella Talent – Healthcare Recruitment Pull Up Banner</title>
<link rel="stylesheet" href="https://fonts.googleapis.com/css2?family=Anton&family=Poppins:wght@500;600&display=swap">
<style>
  :root {
    --page-bg: #e6e6e6;
    --banner-cyan: #4ccbe0;
    --brand-blue: #2231c9;
    --ink: #0d0d0d;
    --footer-black: #1c1c1c;
    --white: #ffffff;
    --art-light: #8fdbe8;
    --art-mid: #5fc4d6;
  }
  * { box-sizing: border-box; margin: 0; padding: 0; }
  html, body {
    width: 1090px; height: 1200px; overflow: hidden;
    background: var(--page-bg);
  }
  .banner {
    position: absolute; left: 297px; top: 20px;
    width: 495px; height: 1160px;
    background: var(--banner-cyan);
    overflow: hidden;
    font-family: "Poppins", sans-serif;
  }
  .banner > * { position: absolute; }
  .centered { left: 0; width: 100%; text-align: center; }

  .display {
    font-family: "Anton", sans-serif; line-height: 1; text-transform: uppercase;
    font-weight: 400;
  }
  .display-wide { display: inline-block; transform: scaleX(1.24); transform-origin: center; }

  .brand-name {
    top: 40px; font-weight: 600;
    font-size: 34px; letter-spacing: 4px; color: var(--ink); line-height: 1;
  }

  .headline { top: 126px; }
  .headline-line { display: block; font-size: 58px; height: 62px; line-height: 62px; }
  .headline .line-1 { color: var(--brand-blue); }
  .headline .line-2 { color: var(--ink); }
  .headline .line-3 { color: var(--brand-blue); }

  .dot-row { top: 314px; display: flex; justify-content: center; gap: 8px; }
  .dot-row span { width: 8px; height: 8px; border-radius: 50%; background: var(--ink); }

  .tagline {
    top: 334px; font-weight: 600; font-size: 19px; color: var(--brand-blue);
  }

  .illustration {
    left: 69px; top: 372px; width: 378px; height: 314px;
    border-radius: 40px;
    background: radial-gradient(ellipse at 55% 45%, var(--art-light), var(--art-mid) 70%, var(--banner-cyan));
  }

  .eyebrow {
    top: 714px; font-weight: 500; font-size: 14px; letter-spacing: 2.2px;
    color: var(--ink); text-transform: uppercase;
  }
  .subhead { font-size: 34px; }
  .subhead-dark { top: 736px; color: var(--ink); }
  .subhead-blue { top: 774px; color: var(--brand-blue); }

  .side-bar { top: 834px; width: 36px; height: 113px; background: var(--brand-blue); }
  .side-bar.left { left: 0; }
  .side-bar.right { right: 0; }

  .specialty {
    top: 834px; width: 115px; height: 113px;
    border: 2px solid var(--brand-blue);
    display: flex; align-items: center; justify-content: center;
    text-align: center; font-weight: 500; font-size: 21px; line-height: 1.25;
    color: var(--ink);
  }
  .specialty.allied { left: 57px; }
  .specialty.nursing { left: 193px; }
  .specialty.medical { left: 325px; }

  .contact-panel {
    left: 0; top: 961px; width: 100%; height: 199px;
    background: var(--footer-black);
  }
  .contact-panel > * { position: absolute; }
  .contact-title { top: 34px; font-size: 34px; color: var(--brand-blue); }
  .contact-line {
    display: flex; align-items: center; justify-content: center; gap: 8px;
    color: var(--white); font-weight: 600; font-size: 18px;
  }
  .contact-web { top: 100px; }
  .contact-social { top: 134px; }
  .icon-dot { width: 18px; height: 18px; border-radius: 50%; background: var(--brand-blue); }
</style>
</head>
<body>
  <main class="banner">
    <div class="brand-name centered">PELLA TALENT</div>

    <h1 class="headline display centered">
      <span class="headline-line line-1"><span class="display-wide">Healthcare</span></span>
      <span class="headline-line line-2"><span class="display-wide">Recruitment</span></span>
      <span class="headline-line line-3"><span class="display-wide">Agency</span></span>
    </h1>

    <div class="dot-row centered"><span></span><span></span><span></span><span></span><span></span></div>
    <p class="tagline centered">Empowering your next career move</p>

    <div class="illustration" role="img" aria-label="Cartoon of medical professionals around a large CV folder with magnifying glass, test tubes and leaves"></div>

    <p class="eyebrow centered">Discover tailored opportunities</p>
    <h2 class="subhead subhead-dark display centered"><span class="display-wide">Based on your</span></h2>
    <h2 class="subhead subhead-blue display centered"><span class="display-wide">Career preferences</span></h2>

    <div class="side-bar left"></div>
    <div class="specialty allied">Allied<br>health</div>
    <div class="specialty nursing">Nursing</div>
    <div class="specialty medical">Medical</div>
    <div class="side-bar right"></div>

    <footer class="contact-panel">
      <h3 class="contact-title display centered"><span class="display-wide">Get in touch</span></h3>
      <div class="contact-line contact-web centered">
        <svg width="20" height="20" viewBox="0 0 20 20" aria-hidden="true" fill="none" stroke="var(--brand-blue)" stroke-width="1.6">
          <circle cx="10" cy="10" r="8.5"/>
          <ellipse cx="10" cy="10" rx="3.6" ry="8.5"/>
          <path d="M1.5 10h17M3 5.5h14M3 14.5h14"/>
        </svg>
        <span>www.pellatalent.com.au</span>
      </div>
      <div class="contact-line contact-social centered">
        <span class="icon-dot"></span>
        <span>@pellatalent</span>
      </div>
    </footer>
  </main>
</body>
</html>
```